QV Pathway Branding
Stationary - Business Card, Letter Head, Powerpoint file, Word Document, Email Signature.
QV Pathway Branding - Information Technology
Creative Brief
Professional
Darren M. L.
Founder
58 Ravel Pine Street #04-12 Orlan Plaza Singapore 142390
darrenm.l@qvpathway-example.com
www.qvpathway-example.com
BRN : 209874163K
The main idea of this contest is not just for the name card but a branding for our stationary. The following are the pointers/comments. I would like it if Icons were used Instead of Phone, Fax, Email, Web. Note: the 2 different Phone numbers in the Cell phone, each should have it's own line if possible. Please use white matte background. For additional effects on the namecard, you may use the different shades to create the effect. For Stationary, please ensure a word document format, powerpoint and email signature format is created as well as the other conventional document types. BRN is only required on the Letterheads. Extra type of formats for branding (e.g. Folder design) earns you extra Stars and ultimately seals the deal with creativity.
Please be creative in the design of the back of the business card. You are to freely manipulate the details given for back and front. Which means you may incorporate in the details in the design to be either the front and or the back.

```html
<!DOCTYPE html>
<html lang="en">
<head>
<meta charset="utf-8">
<title>QV Pathway Branding – Stationery</title>
<link rel="stylesheet" href="https://fonts.googleapis.com/css2?family=Oswald:wght@500&family=Open+Sans:wght@400;600&display=swap">
<style>
  :root{
    --stage:#1c1c1e;
    --stage-line:#242426;
    --paper:#ffffff;
    --ink:#3a3a3a;
    --muted:#8a8a8a;
    --red:#c8141b;
    --red-deep:#8e0d12;
    --red-bright:#e01e25;
    --black:#111111;
    --faint:#e4e4e4;
  }
  *{box-sizing:border-box;margin:0;padding:0}
  html,body{width:1200px;height:336px;overflow:hidden}
  body{
    position:relative;
    background:repeating-linear-gradient(90deg,var(--stage) 0 6px,var(--stage-line) 6px 8px);
    font-family:"Open Sans",Arial,sans-serif;color:var(--ink);
  }
  .piece{position:absolute;box-shadow:0 2px 6px rgba(0,0,0,.6)}
  .wordmark{font-family:"Oswald","Arial Narrow",sans-serif;font-weight:500;letter-spacing:.5px;color:var(--ink);display:flex;align-items:center;gap:4px;line-height:1}
  .wordmark .mark-square{width:.8em;height:.8em;border:1.5px solid var(--red)}
  .wordmark--light{color:var(--paper)}
  .wordmark--light .mark-square{border-color:var(--paper)}
  .tagline{background:var(--red);color:var(--paper);font-size:5px;padding:1px 4px;display:inline-block}

  /* business cards */
  .card{width:138px;height:82px;background:var(--paper)}
  .card--front{left:12px;top:50px;padding:18px 12px}
  .card--front .wordmark{font-size:17px}
  .card--details{left:160px;top:50px;padding:8px 9px;font-size:4.3px;line-height:1.45}
  .card--details .wordmark{font-size:8px;margin-bottom:4px}
  .card--details .name{font-weight:600;font-size:5.5px;color:var(--red)}
  .contact-line{display:flex;align-items:center;gap:3px}
  .contact-line svg{width:5px;height:5px;fill:var(--red)}
  .card--logo{left:12px;top:205px;display:flex;flex-direction:column;align-items:center;justify-content:center;gap:3px}
  .card--logo .wordmark{font-size:12px}
  .card--dark{left:160px;top:205px;background:var(--black);display:flex;align-items:flex-end;justify-content:flex-end;padding:8px}
  .card--dark .wordmark{font-size:8px}

  /* letterhead */
  .letterhead{left:300px;top:19px;width:192px;height:293px;background:var(--paper);padding:12px 12px}
  .letterhead .wordmark{font-size:10px}
  .letterhead .head{display:flex;justify-content:space-between}
  .letterhead .head-contact{font-size:3.6px;line-height:1.5;color:var(--muted);text-align:right}
  .letterhead .watermark{position:absolute;left:66px;top:200px;width:60px;height:60px;border:5px solid var(--faint)}
  .letterhead .foot{position:absolute;left:12px;right:12px;bottom:8px;border-top:1px solid var(--red);padding-top:2px;font-size:3.6px;color:var(--muted);display:flex;justify-content:space-between}

  /* envelopes */
  .envelope{left:504px;width:264px;background:var(--paper);overflow:hidden}
  .envelope--mono{top:95px;height:105px}
  .envelope--red{top:208px;height:95px}
  .envelope svg.flap{position:absolute;left:0;top:0;width:100%;height:100%}
  .envelope .wordmark{position:absolute;font-size:8px}
  .envelope--mono .wordmark{left:120px;top:46px}
  .envelope--red .wordmark{left:14px;top:46px}
  .envelope .address{position:absolute;left:14px;top:60px;font-size:3.6px;line-height:1.5;color:var(--muted)}

  /* folder */
  .folder{left:792px;top:36px;width:396px;height:276px;display:flex}
  .folder__back{width:190px;height:100%;background:linear-gradient(135deg,var(--red-deep),var(--red));position:relative}
  .folder__back .watermark{position:absolute;left:55px;top:98px;width:80px;height:80px;border:8px solid rgba(255,255,255,.15)}
  .folder__back .folder-contact{position:absolute;left:12px;bottom:12px;font-size:4px;line-height:1.5;color:rgba(255,255,255,.75)}
  .folder__front{flex:1;background:linear-gradient(160deg,var(--red-bright),var(--red));position:relative}
  .folder__front .label{position:absolute;left:20px;top:18px;background:var(--paper);padding:6px 8px}
  .folder__front .label .wordmark{font-size:14px}
  .folder__front .label .tagline{margin-top:3px}
  .folder__front .watermark{position:absolute;left:60px;top:98px;width:90px;height:90px;border:9px solid rgba(255,255,255,.12)}
</style>
</head>
<body>

<!-- business cards -->
<section class="piece card card--front">
  <div class="wordmark">QV PATHWAY<span class="mark-square"></span></div>
  <span class="tagline">Vision. Strategy. Growth.</span>
</section>

<section class="piece card card--details">
  <div class="wordmark">QV PATHWAY<span class="mark-square"></span></div>
  <p class="name">Darren M. L.</p>
  <p>Founder</p>
  <p class="contact-line"><svg viewBox="0 0 10 10"><rect x="3" y="0" width="4" height="10" rx="1"/></svg>+65 9123 4567</p>
  <p class="contact-line"><svg viewBox="0 0 10 10"><rect x="3" y="0" width="4" height="10" rx="1"/></svg>+65 9123 4568</p>
  <p class="contact-line"><svg viewBox="0 0 10 10"><rect x="0" y="2" width="10" height="6"/></svg>darrenm.l@qvpathway-example.com</p>
  <p class="contact-line"><svg viewBox="0 0 10 10"><circle cx="5" cy="5" r="5"/></svg>www.qvpathway-example.com</p>
  <p>58 Ravel Pine Street #04-12 Orlan Plaza Singapore 142390</p>
</section>

<section class="piece card card--logo">
  <div class="wordmark">QV PATHWAY<span class="mark-square"></span></div>
</section>

<section class="piece card card--dark">
  <div class="wordmark wordmark--light">QV PATHWAY<span class="mark-square"></span></div>
</section>

<!-- letterhead -->
<section class="piece letterhead">
  <div class="head">
    <div class="wordmark">QV PATHWAY<span class="mark-square"></span></div>
    <div class="head-contact">
      <p>58 Ravel Pine Street #04-12</p>
      <p>Orlan Plaza Singapore 142390</p>
      <p>+65 6123 4567</p>
      <p>www.qvpathway-example.com</p>
    </div>
  </div>
  <div class="watermark"></div>
  <div class="foot"><span>www.qvpathway-example.com</span><span>BRN : 209874163K</span></div>
</section>

<!-- envelopes -->
<section class="piece envelope envelope--mono">
  <svg class="flap" viewBox="0 0 264 105" preserveAspectRatio="none"><polygon points="0,0 264,0 132,40" fill="#111111"/></svg>
  <div class="wordmark">QV PATHWAY<span class="mark-square"></span></div>
</section>

<section class="piece envelope envelope--red">
  <svg class="flap" viewBox="0 0 264 95" preserveAspectRatio="none"><polygon points="0,0 264,0 264,14 132,36 0,14" fill="#c8141b"/></svg>
  <div class="wordmark">QV PATHWAY<span class="mark-square"></span></div>
  <div class="address"><p>58 Ravel Pine Street #04-12</p><p>Orlan Plaza Singapore 142390</p></div>
</section>

<!-- presentation folder -->
<section class="piece folder">
  <div class="folder__back">
    <div class="watermark"></div>
    <div class="folder-contact">
      <p>58 Ravel Pine Street #04-12 Orlan Plaza Singapore 142390</p>
      <p>www.qvpathway-example.com</p>
    </div>
  </div>
  <div class="folder__front">
    <div class="label">
      <div class="wordmark">QV PATHWAY<span class="mark-square"></span></div>
      <span class="tagline">Vision. Strategy. Growth.</span>
    </div>
    <div class="watermark"></div>
  </div>
</section>

</body>
</html>
```